Automotive debt collection business need several banners for new website

We are a debt recovery company called Kelvane Receivables Ltd who work specifically within the car automotive industry acting on behalf of our clients to recover debt which is owed to them. The advantage to using a company such as KVR is that it allows our clients the ability to outsource the work, removing the headache of dealing with the general public and reduces internal staff/overhead costs.
We collect various types of debt including:
Excess Mileage - this is charged when an individual has exceeded their permitted mileage allowance. This is calculated on a pence per mile basis on the mileage over the limit set when the contract was signed.
Damage - charged when a vehicle sustains more damage than is permitted within the contract. Damage could be dents to bodywork, large scratches, torn seats etc. Every area of damage over and above the allowed levels is detailed via a 'Damage Report' and a cost associated to that area of damage. The individual costs are then added up and a total charge formulated. The customer is liable to pay these charges as they have not cared for the vehicle in the appropriate manner whilst under their control
End of Contract Arrears - Once a contract ends and a vehicle is returned to our clients, there may be other charges that need to be repaid that remain outstanding.
We collect debt using a simple process. 1 - The customer is sent a letter as soon as the vehicle is collected advising them of the value of the debt. 2 - A few days later, we attempt to make contact via telephone or email. 3 - Once we contact the customer, we explain the debt and how the figure has been formulated (which is also explain in their letters). 4 - We negotiate (where appropriate) and agree a settlement figure. 5 - The customer pays the debt either in one installment over over a short payment plan.
Our new website (test URL only - http://testing.kelvanereceivables.co.uk/) has a dual purpose. Firstly its to help promote our services to new clients who may be in the market for an alternative supplier (as far as we are aware, we are the only dedicated automotive debt collection company in the UK) and secondly, as a site to help those who owe money to pay and understand who we are (and that we are a registered, legal debt collection company)
Unlike other debt collection websites, we do not want generic images of people shaking hands, smiling etc. We want the images to be visually striking and make the website stand out from the competition. We are happy for these to be graphics rather than images.
We require some visual banners to represent what we do as a business and to emphasis that we specifically collect debt for the automotive sector.
These are websites that contain banners that we are NOT looking for:
http://uk.zintaro-group.com/consumers/contact-data-working-hours/ - bland images of call centers/random people on phones etc
http://www.pellowmarsh.com/client/
These are websites that contain banners that we class as OK:
http://www.quorvath.co.uk/business-services/debt-collection.html - fairly clear way of explaining their services
http://www.estatearrears.co.uk/ - a slightly different slant using non-related images to explain what they can and cant do
http://www.wqlholdings.com/home/#.UhNNeD98CL0 - uses text to text banners to explain their offering
We require:
x4 - 870px X 500px - these will appear on the main homepage and rotate
x2 - 270px X 240px - static images that will to the right of the home page. One image needs to indicate some type of payment method as its a link to our online payment system, the second image refers to our other services (see the appropriate page on the website) these additional services include asset recovery, inspection, bespoke software solutions for the asset industry and auction disposal
x3 - 90px X 90px - Static images to represent payment methods that include cheque/card/bank transfer (see website for more info)
Our corporate colours are Black/Red/Grey
Depending on the designs received, we expect 2 rounds of modifications and we will advise those designers that have not been successful with positive feedback. We guarantee to pay the successful designer but work must be completed and ALL requested material produced and approved.

```html
<!DOCTYPE html>
<html lang="en">
<head>
<meta charset="utf-8">
<title>Damage – charged collecting | Kelvane Receivables</title>
<link rel="stylesheet" href="https://fonts.googleapis.com/css2?family=Open+Sans:wght@400;600&display=swap">
<style>
  :root {
    --red: #d4000d;
    --red-deep: #8e0008;
    --black: #141414;
    --grey-light: #ececec;
    --grey-mid: #cfcfcf;
    --grey-dark: #4a4a4a;
    --white: #ffffff;
    --ink: #1b1b1b;
  }
  html, body {
    margin: 0;
    padding: 0;
    width: 1200px;
    height: 690px;
    overflow: hidden;
    background: var(--grey-light);
  }
  .banner {
    position: relative;
    width: 1200px;
    height: 690px;
    overflow: hidden;
    font-family: "Open Sans", "Segoe UI", sans-serif;
    background: linear-gradient(180deg, #f2f2f2 0%, #e6e6e6 100%);
  }
  .scene-photo {
    position: absolute;
    inset: 0;
    background:
      radial-gradient(circle at 830px 330px, rgba(90,90,90,0.35) 0, rgba(150,150,150,0.12) 120px, transparent 380px),
      radial-gradient(ellipse 420px 160px at 360px 320px, rgba(70,70,70,0.45) 0, rgba(160,160,160,0.18) 60%, transparent 100%),
      radial-gradient(circle at 150px 240px, rgba(110,140,140,0.35) 0, transparent 170px);
  }
  .title-band {
    position: absolute;
    left: 0;
    top: 50px;
    width: 800px;
    height: 112px;
  }
  .title-band__rule {
    position: absolute;
    left: 0;
    top: 0;
    width: 100%;
    height: 9px;
    background: linear-gradient(90deg, var(--black) 0%, var(--black) 70%, transparent 100%);
  }
  .title-band__fill {
    position: absolute;
    left: 0;
    top: 12px;
    width: 100%;
    height: 76px;
    background: linear-gradient(90deg, var(--red) 0%, var(--red) 62%, rgba(212,0,13,0.6) 80%, transparent 100%);
  }
  .title-band__base {
    position: absolute;
    left: 0;
    top: 92px;
    width: 100%;
    height: 18px;
    background: linear-gradient(90deg, var(--black) 0%, var(--black) 65%, transparent 100%);
  }
  .title {
    position: absolute;
    left: 32px;
    top: 12px;
    margin: 0;
    line-height: 76px;
    font-size: 50px;
    font-weight: 400;
    color: var(--white);
    letter-spacing: 0.5px;
    text-shadow: 0 1px 2px rgba(0,0,0,0.35);
  }
  .checklist-icon {
    position: absolute;
    left: 945px;
    top: 58px;
    width: 150px;
    height: 170px;
  }
  .pitch {
    position: absolute;
    left: 0;
    top: 390px;
    width: 738px;
    height: 146px;
    background: rgba(255,255,255,0.78);
    box-sizing: border-box;
    padding: 8px 0 0 12px;
  }
  .pitch p {
    margin: 0;
    font-size: 25px;
    line-height: 41px;
    color: var(--ink);
  }
  .footer-band {
    position: absolute;
    left: 0;
    top: 556px;
    width: 1200px;
    height: 134px;
  }
  .footer-band svg { display: block; }
  .footer-title {
    position: absolute;
    left: 0;
    top: 16px;
    width: 100%;
    margin: 0;
    text-align: center;
    font-size: 64px;
    font-weight: 400;
    line-height: 80px;
    color: var(--white);
    letter-spacing: 1px;
    -webkit-text-stroke: 2px #2a2a2a;
    paint-order: stroke fill;
    text-shadow: 0 2px 3px rgba(0,0,0,0.4);
  }
</style>
</head>
<body>
  <main class="banner">
    <div class="scene-photo" role="img" aria-label="Photograph of a shattered windscreen with a damaged car blurred behind the cracked glass"></div>

    <header class="title-band">
      <div class="title-band__rule"></div>
      <div class="title-band__fill"></div>
      <div class="title-band__base"></div>
      <h1 class="title">Damage – charged collecting</h1>
    </header>

    <svg class="checklist-icon" viewBox="0 0 150 170" aria-hidden="true">
      <rect x="18" y="22" width="112" height="140" rx="10" fill="#b5651d" stroke="#6b3a10" stroke-width="3"/>
      <rect x="32" y="38" width="84" height="112" fill="#f7f7f7" stroke="#bbbbbb" stroke-width="2"/>
      <rect x="50" y="12" width="48" height="22" rx="5" fill="#9a9a9a" stroke="#555" stroke-width="2"/>
      <rect x="48" y="66" width="44" height="44" fill="none" stroke="#333" stroke-width="4"/>
      <path d="M52 86 L68 104 L128 40 L136 50 L70 124 L44 94 Z" fill="var(--red)" stroke="#7a0006" stroke-width="2"/>
    </svg>

    <section class="pitch">
      <p>KVR Receivables only collect debt</p>
      <p>from within the automotive and asset sector</p>
      <p>ensuring consistent above-average recovery rates</p>
    </section>

    <footer class="footer-band">
      <svg width="1200" height="134" viewBox="0 0 1200 134" aria-hidden="true">
        <rect x="0" y="0" width="1200" height="6" fill="var(--grey-mid)"/>
        <rect x="0" y="12" width="1200" height="80" fill="var(--red)"/>
        <rect x="0" y="86" width="1200" height="8" fill="var(--red-deep)"/>
        <rect x="0" y="94" width="1200" height="40" fill="var(--grey-light)"/>
        <path d="M150 26 L1050 26 L1090 64 L1090 100 L110 100 L110 64 Z" fill="none" stroke="var(--white)" stroke-width="3"/>
        <path d="M160 34 L1040 34 L1078 68 L1078 100 L122 100 L122 68 Z" fill="var(--black)"/>
      </svg>
      <p class="footer-title">Automotive debt collecting</p>
    </footer>
  </main>
</body>
</html>
```